looking for sleek business card to standout from the crowd!

We are a young biotechnology company looking to help you personalize your health through understanding your genetic make up. We need you help in making a clean but sleek business card design using our new logo. The goal? Any time we give our cards out, people say "nice card!" The feel we are going for is "modern-techy". We don't want to come across as an old, giant pharma company, but not trying to be a hipster either.

Target Market(s)

healthcare and biotechnology industry.

Industry/Entity Type

Biotechnology

Contact Information for Business Card

Info to include on the card will be NAME, TITLE, EMAIL, PHONE. The companies website (www.corvalinbio.com) should also be on the card some where. Would like the logo, when printed, to be raised.

Requirements
Must have
• The logo we have attached in the color it is in. Fonts for text should lean toward more professional/tech.
Nice to have
• Prefer white/light color background
Should not have
• cartoons, landscape backgrounds images.

```html
<!DOCTYPE html>
<html lang="en">
<head>
<meta charset="utf-8">
<title>Corvalin Business Card</title>
<link href="https://fonts.googleapis.com/css2?family=Montserrat:wght@700;800&family=Quicksand:wght@500;600&display=swap" rel="stylesheet">
<style>
  :root {
    --blue: #0784d2;
    --blue-light: #1ea0e6;
    --green: #8ed44f;
    --green-dark: #6fc23a;
    --white: #ffffff;
    --ink-blue: #0a78c2;
    --stage: #34303f;
  }
  * { margin: 0; padding: 0; box-sizing: border-box; }
  html, body { width: 1200px; height: 800px; overflow: hidden; }
  body {
    background: var(--stage);
    display: flex;
    align-items: center;
    justify-content: center;
    gap: 40px;
  }
  .card {
    position: relative;
    width: 540px;
    height: 310px;
    overflow: hidden;
    box-shadow: 0 14px 30px rgba(0,0,0,0.35);
  }
  .card-art { position: absolute; inset: 0; width: 100%; height: 100%; display: block; }

  /* Back: contact face */
  .identity {
    position: absolute;
    left: 34px;
    top: 14px;
    color: var(--ink-blue);
  }
  .identity-name {
    font-family: "Montserrat", sans-serif;
    font-weight: 800;
    font-size: 34px;
    letter-spacing: 1px;
    line-height: 1;
  }
  .identity-title {
    font-family: "Quicksand", sans-serif;
    font-weight: 500;
    font-size: 17px;
    margin-top: 2px;
  }
  .contact-list {
    position: absolute;
    left: 28px;
    top: 104px;
    list-style: none;
  }
  .contact-item {
    display: flex;
    align-items: center;
    gap: 10px;
    height: 34px;
    color: var(--white);
    font-family: "Quicksand", sans-serif;
    font-weight: 600;
    font-size: 15px;
    letter-spacing: 0.3px;
  }
  .contact-icon {
    width: 26px;
    height: 26px;
    flex: none;
  }

  /* Front: brand face */
  .brand {
    position: absolute;
    left: 0;
    top: 60px;
    width: 360px;
    height: 90px;
    display: flex;
    align-items: center;
    justify-content: center;
    gap: 12px;
  }
  .brand-name {
    font-family: "Montserrat", sans-serif;
    font-weight: 800;
    font-size: 44px;
    letter-spacing: 2px;
    color: var(--ink-blue);
  }
  .brand-dot {
    width: 22px;
    height: 22px;
    border-radius: 50%;
    background: var(--green);
  }
</style>
</head>
<body>

  <!-- Contact face -->
  <section class="card card--contact" aria-label="Business card contact side">
    <svg class="card-art" viewBox="0 0 540 310" aria-hidden="true">
      <rect width="540" height="310" fill="var(--white)"/>
      <rect y="86" width="540" height="182" fill="var(--blue)"/>
      <rect y="82" width="540" height="5" fill="var(--green)"/>
      <rect y="268" width="540" height="30" fill="var(--green)"/>
      <polygon points="388,0 404,0 364,155 404,310 388,310 348,155" fill="var(--green-dark)"/>
      <polygon points="404,0 440,0 400,155 440,310 404,310 364,155" fill="var(--white)"/>
      <polygon points="440,0 470,0 430,155 470,310 440,310 400,155" fill="var(--blue-light)"/>
      <polygon points="470,0 540,0 540,310 470,310 430,155" fill="var(--white)"/>
    </svg>

    <div class="identity">
      <div class="identity-name">NAME</div>
      <div class="identity-title">Postion/ Title</div>
    </div>

    <ul class="contact-list">
      <li class="contact-item">
        <svg class="contact-icon" viewBox="0 0 26 26" aria-hidden="true">
          <circle cx="13" cy="13" r="11.5" fill="none" stroke="var(--green)" stroke-width="2"/>
          <path d="M8 10.5c0-2 2-3 5-3s5 1 5 3l-2 .5-.5-1.5h-5l-.5 1.5z M9.5 12h7l1 5h-9z" fill="var(--white)"/>
        </svg>
        Phone number
      </li>
      <li class="contact-item">
        <svg class="contact-icon" viewBox="0 0 26 26" aria-hidden="true">
          <circle cx="13" cy="13" r="11.5" fill="none" stroke="var(--green)" stroke-width="2"/>
          <rect x="7" y="9" width="12" height="8" fill="none" stroke="var(--white)" stroke-width="1.4"/>
          <path d="M7 9l6 5 6-5" fill="none" stroke="var(--white)" stroke-width="1.4"/>
        </svg>
        Email
      </li>
      <li class="contact-item">
        <svg class="contact-icon" viewBox="0 0 26 26" aria-hidden="true">
          <circle cx="13" cy="13" r="11.5" fill="none" stroke="var(--green)" stroke-width="2"/>
          <circle cx="13" cy="13" r="6" fill="none" stroke="var(--white)" stroke-width="1.3"/>
          <ellipse cx="13" cy="13" rx="2.6" ry="6" fill="none" stroke="var(--white)" stroke-width="1.1"/>
          <path d="M7 13h12M8 10h10M8 16h10" stroke="var(--white)" stroke-width="1"/>
        </svg>
        web address
      </li>
      <li class="contact-item">
        <svg class="contact-icon" viewBox="0 0 26 26" aria-hidden="true">
          <circle cx="13" cy="13" r="11.5" fill="none" stroke="var(--green)" stroke-width="2"/>
          <path d="M7 13l6-5.5 6 5.5M8.5 12v6h9v-6M11.5 18v-3.5h3V18" fill="none" stroke="var(--white)" stroke-width="1.4"/>
        </svg>
        physical address
      </li>
    </ul>
  </section>

  <!-- Brand face -->
  <section class="card card--brand" aria-label="Business card brand side">
    <svg class="card-art" viewBox="0 0 540 310" aria-hidden="true">
      <rect width="540" height="310" fill="var(--blue)"/>
      <rect y="52" width="540" height="3" fill="var(--green)"/>
      <rect y="60" width="540" height="90" fill="var(--white)"/>
      <rect y="156" width="540" height="3" fill="var(--green)"/>
      <polygon points="388,0 404,0 364,155 404,310 388,310 348,155" fill="var(--green-dark)"/>
      <polygon points="404,0 440,0 400,155 440,310 404,310 364,155" fill="var(--white)"/>
      <polygon points="440,0 470,0 430,155 470,310 440,310 400,155" fill="var(--blue-light)"/>
      <polygon points="470,0 540,0 540,310 470,310 430,155" fill="var(--white)"/>
    </svg>

    <div class="brand">
      <span class="brand-name">CORVALIN</span>
      <span class="brand-dot"></span>
    </div>
  </section>

</body>
</html>
```